A picture showing off our Million Dollar Renovation Update at Maple Rapids Splashpark Lodge

Use the uploaded images to develop a picture at least 1366x512 with text saying - Check out our Million Dollar Renovation - I have uploaded alot please use the best to show off . It will go as the hero picture on this website https://maplerapidslodge.example/ - would also to use in social in a "splash" manner to show off updates

Target Market(s)

visitors to our website and past guest

Industry/Entity Type

Hotel

Requirements
Must have
• Check out Our Million Dollar Renovation!
Nice to have
• pictures

```html
<!DOCTYPE html>
<html lang="en">
<head>
<meta charset="utf-8">
<title>Maple Rapids Splashpark Lodge – Renovation Hero Variations</title>
<link href="https://fonts.googleapis.com/css2?family=Jost:wght@300;400&family=Roboto:wght@400;500&display=swap" rel="stylesheet">
<style>
  :root {
    --board: #ffffff;
    --header-bg: #eef0fa;
    --navy: #2b3d6e;
    --navy-deep: #1f2f5c;
    --orange: #f47b2a;
    --white: #ffffff;
    --label-grey: #8a8f98;
    --field-border: #c9ccd4;
    --footer-band: #000000;
    --room-window: #8fa3a0;
    --room-wall: #4f7a55;
    --room-bed: #5e9a8a;
    --room-dark: #2e2b2c;
  }
  * { box-sizing: border-box; margin: 0; padding: 0; }
  html, body { width: 804px; height: 1200px; overflow: hidden; background: var(--board); }
  .board { position: relative; width: 804px; height: 1200px; }

  .mockup {
    position: absolute; left: 62px; width: 678px; height: 422px;
    background: var(--white);
    box-shadow: 0 10px 36px rgba(0,0,0,0.18);
    overflow: hidden;
    font-family: "Roboto", Arial, sans-serif;
  }
  .mockup--one { top: 69px; }
  .mockup--two { top: 592px; }

  .variation-label {
    position: absolute; left: 73px;
    font-family: "Jost", sans-serif; font-weight: 300;
    font-size: 13px; letter-spacing: 3.5px; color: var(--label-grey);
  }

  .site-header { position: absolute; left: 0; top: 0; width: 678px; height: 83px; background: var(--header-bg); }
  .brand { position: absolute; left: 146px; top: 18px; display: flex; align-items: center; gap: 8px; }
  .brand-dot { width: 34px; height: 34px; border-radius: 50%; background: var(--navy); flex: none; }
  .brand-name { font-weight: 500; font-size: 15px; line-height: 18px; color: var(--navy-deep); width: 150px; }
  .site-phone { position: absolute; left: 500px; top: 32px; font-size: 16px; color: var(--navy-deep); }

  .site-nav { position: absolute; left: 0; top: 83px; width: 678px; height: 27px; background: var(--navy); }
  .nav-item { position: absolute; top: 0; line-height: 27px; font-size: 11px; color: var(--orange); transform: translateX(-50%); white-space: nowrap; }
  .nav-book { position: absolute; left: 540px; top: 0; width: 138px; height: 27px; background: var(--orange); color: var(--navy); font-size: 11px; line-height: 27px; text-align: center; }

  .hero { position: absolute; left: 0; top: 110px; width: 678px; height: 257px; overflow: hidden; }
  .hero-photo {
    position: absolute; inset: 0;
    background:
      linear-gradient(180deg, rgba(0,0,0,0) 55%, rgba(30,40,35,0.25) 100%),
      linear-gradient(90deg, var(--room-dark) 0%, var(--room-window) 12%, #9fb39a 25%, var(--room-wall) 42%, var(--room-bed) 60%, #3e3633 78%, var(--room-wall) 100%);
  }
  .hero-frame { position: absolute; left: 0; top: 0; width: 678px; height: 257px; }
  .hero-frame path { fill: none; stroke: var(--white); stroke-width: 3; }
  .mockup--two .hero-frame path { stroke: var(--orange); }
  .hero-kicker, .hero-title {
    position: absolute; left: 0; width: 678px; text-align: center;
    font-family: "Jost", sans-serif; font-weight: 300; color: var(--white); text-transform: uppercase;
    line-height: 1;
  }
  .hero-kicker { top: 49px; font-size: 16px; letter-spacing: 1.5px; }
  .hero-title { top: 79px; font-size: 26px; letter-spacing: 1.8px; }
  .hero-wave { position: absolute; left: 0; top: 0; width: 678px; height: 257px; }

  .booking { position: absolute; left: 0; top: 367px; width: 678px; height: 55px; display: flex; align-items: center; justify-content: center; gap: 12px; padding-top: 20px; font-size: 9.5px; color: var(--navy-deep); }
  .field { display: flex; align-items: center; gap: 4px; }
  .field-box { height: 12px; border: 1px solid var(--field-border); font-size: 7.5px; line-height: 10px; padding: 0 3px; color: #444; background: var(--white); }
  .field-box--date { width: 66px; }
  .field-box--num { width: 12px; text-align: center; padding: 0; }
  .booking-button { background: var(--orange); color: var(--navy-deep); font-size: 9.5px; padding: 1px 4px; border: 1px solid #d9651a; }

  .footer-band { position: absolute; left: 0; top: 1109px; width: 804px; height: 91px; background: var(--footer-band); }
</style>
</head>
<body>
<main class="board">

  <section class="mockup mockup--one" aria-label="Homepage hero, white frame">
    <header class="site-header">
      <div class="brand"><span class="brand-dot"></span><span class="brand-name">Maple Rapids Splashpark Lodge</span></div>
      <div class="site-phone">1-800-555-0142</div>
    </header>
    <nav class="site-nav">
      <span class="nav-item" style="left:73px">Guest Rooms</span>
      <span class="nav-item" style="left:212px">Waterpark</span>
      <span class="nav-item" style="left:341px">Discounts</span>
      <span class="nav-item" style="left:472px">Recreation</span>
      <span class="nav-book">Book Now!</span>
    </nav>
    <div class="hero">
      <div class="hero-photo" role="img" aria-label="Renovated guest room with a king bed, teal quilt, dark headboard, green wall and a window with patterned curtains"></div>
      <svg class="hero-frame" viewBox="0 0 678 257" aria-hidden="true">
        <path d="M248,56.5 H93.5 V130.5 H587.5 V56.5 H432"/>
      </svg>
      <svg class="hero-wave" viewBox="0 0 678 257" aria-hidden="true">
        <path d="M0,257 L0,228 C150,168 350,174 480,204 C560,222 630,224 678,212 L678,257 Z" fill="#ffffff"/>
        <path d="M0,257 L0,246 C150,190 340,196 470,222 C560,240 630,246 678,240 L678,257 Z" fill="#2b3d6e"/>
        <path d="M0,257 C120,214 260,214 380,240 C420,249 450,254 478,257 Z" fill="#f47b2a"/>
      </svg>
      <p class="hero-kicker">Check out our</p>
      <h1 class="hero-title">Million Dollar Renovation</h1>
    </div>
    <form class="booking">
      <span class="field">Arrival Date: <span class="field-box field-box--date">16/09/2018</span></span>
      <span class="field"># of Nights: <span class="field-box field-box--num">2</span></span>
      <span class="field"># of Adults: <span class="field-box field-box--num">2</span></span>
      <span class="field"># of Children: <span class="field-box field-box--num">0</span></span>
      <span class="booking-button">Book Direct!</span>
    </form>
  </section>
  <p class="variation-label" style="top:518px">VARIATION 1</p>

  <section class="mockup mockup--two" aria-label="Homepage hero, orange frame">
    <header class="site-header">
      <div class="brand"><span class="brand-dot"></span><span class="brand-name">Maple Rapids Splashpark Lodge</span></div>
      <div class="site-phone">1-800-555-0142</div>
    </header>
    <nav class="site-nav">
      <span class="nav-item" style="left:73px">Guest Rooms</span>
      <span class="nav-item" style="left:212px">Waterpark</span>
      <span class="nav-item" style="left:341px">Discounts</span>
      <span class="nav-item" style="left:472px">Recreation</span>
      <span class="nav-book">Book Now!</span>
    </nav>
    <div class="hero">
      <div class="hero-photo" role="img" aria-label="Renovated guest room with a king bed, teal quilt, dark headboard, green wall and a window with patterned curtains"></div>
      <svg class="hero-frame" viewBox="0 0 678 257" aria-hidden="true">
        <path d="M248,56.5 H93.5 V130.5 H587.5 V56.5 H432"/>
      </svg>
      <svg class="hero-wave" viewBox="0 0 678 257" aria-hidden="true">
        <path d="M0,257 L0,228 C150,168 350,174 480,204 C560,222 630,224 678,212 L678,257 Z" fill="#ffffff"/>
        <path d="M0,257 L0,246 C150,190 340,196 470,222 C560,240 630,246 678,240 L678,257 Z" fill="#2b3d6e"/>
        <path d="M0,257 C120,214 260,214 380,240 C420,249 450,254 478,257 Z" fill="#f47b2a"/>
      </svg>
      <p class="hero-kicker">Check out our</p>
      <h1 class="hero-title">Million Dollar Renovation</h1>
    </div>
    <form class="booking">
      <span class="field">Arrival Date: <span class="field-box field-box--date">16/09/2018</span></span>
      <span class="field"># of Nights: <span class="field-box field-box--num">2</span></span>
      <span class="field"># of Adults: <span class="field-box field-box--num">2</span></span>
      <span class="field"># of Children: <span class="field-box field-box--num">0</span></span>
      <span class="booking-button">Book Direct!</span>
    </form>
  </section>
  <p class="variation-label" style="top:1041px">VARIATION 2</p>

  <footer class="footer-band" aria-hidden="true"></footer>

</main>
</body>
</html>
```